Flyer-Design für Mittagsbelieferung
Zielgruppe
Mittags Belieferung ältere Menschen, Firmen, Berufstätige
Aufgabenstellung
Text aus Datei den Bestellzettel nicht weiter beachten nur Seite 2 u.3... Logo vielleicht vorne drauf... Format bin ich unentschieden

```html
<!DOCTYPE html>
<html lang="de">
<head>
<meta charset="utf-8">
<title>Pilvo – Flyer Mittagsbelieferung</title>
<link href="https://fonts.googleapis.com/css2?family=Didact+Gothic&family=Nunito:wght@700;800&family=Roboto+Condensed:wght@400;700&family=Yellowtail&display=swap" rel="stylesheet">
<style>
  :root{
    --stage:#8f8c74;
    --panel:#2f3233;
    --white:#ffffff;
    --green:#3fae3d;
    --red:#c0171b;
    --soft:#e9e9e9;
  }
  *{box-sizing:border-box;margin:0;padding:0}
  html,body{width:1200px;height:1200px;overflow:hidden;background:var(--stage)}
  .canvas{position:relative;width:1200px;height:1200px;overflow:hidden}
  .flyer{position:absolute;top:62px;width:507px;height:1074px;background:var(--panel);color:var(--white);overflow:hidden}
  .flyer--front{left:65px}
  .flyer--back{left:615px}
  .abs{position:absolute}
  .body{font-family:"Didact Gothic",sans-serif}
  .script{font-family:"Yellowtail",cursive}

  /* front */
  .brand{left:0;right:0;top:48px;text-align:center;font-family:"Nunito",sans-serif;font-weight:800;font-size:28px;color:var(--green);letter-spacing:.5px}
  .brand-dot{display:inline-block;width:12px;height:12px;border-radius:50%;background:var(--green);margin-right:8px;vertical-align:middle}
  .tagline{left:0;right:0;top:86px;text-align:center;font-size:17px;color:var(--soft)}
  .mascot{left:168px;top:112px;width:177px;height:160px;border-radius:14px;background:radial-gradient(circle at 50% 45%,#e8772a 0,#c23a2a 55%,#2f3233 82%)}
  .front-phone{left:0;right:0;top:277px;text-align:center;font-family:"Yellowtail",cursive;font-size:24px;color:var(--soft);letter-spacing:.5px}
  .photo{position:absolute}
  .photo--patties{left:0;top:520px;width:242px;height:330px;background:linear-gradient(160deg,#6b4a2e,#7a4c2a 45%,#4a3a2c)}
  .photo--roulade{left:248px;top:385px;width:259px;height:465px;background:linear-gradient(150deg,#e8e6e1 0,#d9c88a 30%,#8a3a22 60%,#5a1f2e 80%,#ece9e4)}
  .plate{left:-2px;top:332px;width:272px;height:272px;border-radius:50%;border:5px solid var(--green);background:radial-gradient(circle,#d68a32 0,#c67625 40%,#1e1e1e 70%)}
  .wave{left:0;top:810px;width:507px;height:80px}
  .area{left:0;right:0;top:908px;text-align:center;font-size:17px;line-height:23.5px;color:var(--soft)}
  .address{left:0;right:0;top:1023px;text-align:center;font-size:17.5px;color:var(--white)}

  /* back */
  .intro{left:0;right:0;top:46px;text-align:center;font-size:23px;line-height:29.5px}
  .dots{left:48px;height:3px;background-image:radial-gradient(circle,var(--green) 1.3px,transparent 1.5px);background-size:7px 3px}
  .icon{left:88px;top:196px;width:76px;height:76px}
  .choice{left:48px;top:290px;font-family:"Nunito",sans-serif;font-weight:700;font-size:16.5px;line-height:23.5px}
  .price{left:234px;top:182px;width:238px;height:238px;border-radius:50%;background:var(--red);text-align:center;font-family:"Roboto Condensed",sans-serif}
  .price-title{margin-top:46px;font-family:"Nunito",sans-serif;font-weight:800;font-size:19px;line-height:20px}
  .price-sub{font-size:13.5px;line-height:15px}
  .price-value{font-weight:700;font-size:52px;line-height:58px;margin-top:2px}
  .price-note{font-size:13.5px;line-height:16.5px;margin-top:4px}
  .pay-head{left:48px;top:468px;font-size:22px;font-weight:400;color:var(--green)}
  .pay-col{top:516px;font-size:16.5px;line-height:23.5px;color:var(--soft)}
  .pay-col strong{font-family:"Nunito",sans-serif;font-weight:700;color:var(--white)}
  .pay-col--cash{left:47px}
  .pay-col--bill{left:269px}
  .teaser{left:48px;width:413px;top:697px;font-size:17px;line-height:23.5px;text-align:justify;color:var(--soft)}
  .hours{left:60px;width:167px;top:858px;text-align:right;font-size:16.5px;line-height:23.5px;color:var(--soft)}
  .divider{left:248px;top:856px;width:2px;height:102px;background:var(--green)}
  .hotline{left:267px;top:858px}
  .hotline-label{font-family:"Nunito",sans-serif;font-weight:700;font-size:16.5px}
  .hotline-number{font-family:"Roboto Condensed",sans-serif;font-weight:700;font-size:30px;color:var(--green);margin-top:8px}
  .hotline-mail{font-family:"Roboto Condensed",sans-serif;font-size:15.5px;margin-top:4px;color:var(--soft)}
  .deadline{left:0;right:0;top:998px;text-align:center;font-size:16.5px;line-height:20px;color:var(--soft)}
</style>
</head>
<body>
<div class="canvas">

  <section class="flyer flyer--front">
    <div class="abs brand"><span class="brand-dot"></span>pilvo</div>
    <div class="abs tagline script">ihr mobiler Mittagstisch aus Selvodorn</div>
    <div class="abs mascot" role="img" aria-label="Illustration: Lieferfigur auf rotem Motorroller mit Teller"></div>
    <div class="abs front-phone">04127/5507320</div>

    <div class="photo photo--patties" role="img" aria-label="Foto: gebratene Frikadellen mit Kräutern"></div>
    <div class="photo photo--roulade" role="img" aria-label="Foto: Rouladen mit Klößen und Rotkohl"></div>
    <div class="abs plate" role="img" aria-label="Foto: Schnitzel mit Zitrone auf schwarzem Teller"></div>

    <svg class="abs wave" viewBox="0 0 507 80" preserveAspectRatio="none" aria-hidden="true">
      <path d="M0 38 C120 30 220 14 330 12 C420 10 470 14 507 16 L507 80 L0 80 Z" fill="var(--panel)"/>
      <path d="M0 38 C120 30 220 14 330 12 C420 10 470 14 507 16 L507 28 C470 26 420 24 330 26 C220 30 120 50 0 62 Z" fill="var(--green)"/>
    </svg>

    <p class="abs area body">Derzeitiges Auslieferungsgebiet<br>Selvodorn-Lehmstedt-Korwitz-Dalmsee-Fernbruch-<br>Hollendorf- Wendemark- Rabensee- Grimmow<br>-Tessenhof -Birkhagen auch weitere möglich</p>
    <p class="abs address body">Pilvo-Restaurant&nbsp; | &nbsp;Birkenallee 7&nbsp; | &nbsp;28914 Selvodorn</p>
  </section>

  <section class="flyer flyer--back">
    <p class="abs intro script">Wir liefern Ihnen gerne Ihr Wunschmenü<br>in unseren Thermoboxen zu Ihnen nach Hause<br>oder auch ins Büro oder Ihren Arbeitsplatz.</p>

    <div class="abs dots" style="top:177px;width:253px"></div>

    <svg class="abs icon" viewBox="0 0 76 76" fill="none" stroke="var(--white)" stroke-width="3" stroke-linecap="round" aria-hidden="true">
      <path d="M26 6c-4 4 4 7 0 11M38 4c-4 4 4 7 0 11M50 6c-4 4 4 7 0 11"/>
      <path d="M6 42h64M10 42l6 22h44l6-22"/>
      <path d="M14 42c-2-8 6-12 10-8 2-6 12-6 14 0 3-5 12-4 12 3 5-2 11 2 9 5"/>
      <path d="M26 70h32"/>
    </svg>

    <p class="abs choice">Sie haben täglich<br>die Wahl zwischen<br>3 Menüs inkl.<br>Nachtisch.</p>

    <div class="abs price">
      <div class="price-title">Preis pro Menü</div>
      <div class="price-sub">inkl. Nachtisch &amp; Lieferung</div>
      <div class="price-value">6,00 €</div>
      <div class="price-note">+ 1 Stück selbstgebackenen<br>Kuchen liefern wir ihnen gerne<br>für 1,50€ mit dazu</div>
    </div>

    <div class="abs dots" style="top:411px;width:230px"></div>

    <h2 class="abs pay-head script">Bei der Bezahlung haben Sie die Wahl zwischen</h2>

    <p class="abs pay-col pay-col--cash body"><strong>Barzahlung</strong><br>immer Montags im<br>Vorraus beim Fahrer<br>gegen Erhalt<br>der Wochenrechnung</p>
    <p class="abs pay-col pay-col--bill body"><strong>Monatsrechnung</strong><br>am Ende des Monats wird<br>Ihnen eine Rechnung für<br>den jeweiligen Monat<br>ausgestellt die Sie dann<br>einfach überweisen.</p>

    <p class="abs teaser body">Fordern sie noch heute einen Speiseplan von uns an, und lassen Sie sich von unseren täglich frisch zubereiteten Speisen überzeugen. Keine Vertragsbindung!! d.h. Sollte es ihnen nicht gefallen können Sie jederzeit wieder abbestellen</p>

    <p class="abs hours body">Auslieferung von<br>Montag - Samstag<br>zwischen 10.30 Uhr<br>und 12.30 Uhr</p>
    <div class="abs divider"></div>
    <div class="abs hotline">
      <div class="hotline-label">Bestellhotline</div>
      <div class="hotline-number">04127/5507320</div>
      <div class="hotline-mail">oder mail an pilvo@postfachwerk.de</div>
    </div>

    <p class="abs deadline body">An-und Abbestellungen sind täglich<br>bis 10.00Uhr möglich</p>
  </section>

</div>
</body>
</html>
```